Tovally's Pest Control Billboard

I need a billboard designed for my pest control company. Feel free to check out our website, www.tovallys-example.com. I can also provide any logo, etc for design help. It should be funny but show trust. We want to focus on Mice and rodents. Phone # 555-013-7291 should be used. Shouldn't be to scary, we never use fear to sell.

Target Market(s)

People with pest issues, Mice, Rodents

Industry/Entity Type

Pest Control

Font styles to use
Sans Serif

Colors
59FF00
82FF00
B8FF75
E3FFCB
F4FFEA

Requirements
Must have
• Humor
Nice to have
• Some humor

```html
<!DOCTYPE html>
<html lang="en">
<head>
<meta charset="utf-8">
<title>Tovally's Pest Control Billboard</title>
<link href="https://fonts.googleapis.com/css2?family=Montserrat:wght@700;800&family=Poppins:wght@400;500&display=swap" rel="stylesheet">
<style>
  :root {
    --stage: #eceff2;
    --paper: #ffffff;
    --ink: #111111;
    --lime: #80c11c;
    --lime-deep: #2f9a12;
    --mint: #f2fbe6;
    --charcoal: #252525;
    --white: #ffffff;
  }
  * { margin: 0; padding: 0; box-sizing: border-box; }
  html, body { width: 1200px; height: 944px; overflow: hidden; }
  body { background: var(--stage); position: relative; font-family: "Montserrat", sans-serif; }

  .billboard {
    position: absolute; left: 0; top: 282px;
    width: 1200px; height: 380px;
    background: var(--paper); overflow: hidden;
  }

  .mint-blob {
    position: absolute; background: var(--mint);
    border-radius: 52% 48% 46% 54% / 58% 46% 54% 42%;
  }
  .mint-blob.left { left: 420px; top: 110px; width: 300px; height: 200px; }
  .mint-blob.right { left: 720px; top: 60px; width: 470px; height: 210px; }

  .brand { position: absolute; left: 40px; top: 22px; }
  .brand-name {
    font-weight: 800; font-size: 30px; color: var(--ink); line-height: 1.1;
    display: flex; align-items: center; gap: 12px;
  }
  .brand-dot { width: 18px; height: 18px; border-radius: 50%; background: var(--lime); }
  .brand-phone {
    margin-top: 8px; margin-left: 30px;
    font-weight: 700; font-size: 16px; color: var(--ink);
  }

  .headline {
    position: absolute; left: 36px; top: 128px;
    font-weight: 800; font-size: 34px; line-height: 1.18; color: var(--ink);
    letter-spacing: -0.3px;
  }
  .headline .accent { color: var(--lime); }

  .quip {
    position: absolute; left: 740px; top: 22px; width: 440px;
    font-weight: 700; font-size: 18px; line-height: 1.3; color: var(--charcoal);
    text-align: right;
  }
  .quip .accent { color: var(--lime-deep); }

  .offer-band {
    position: absolute; left: 0; top: 282px; width: 400px; height: 98px;
    background: var(--charcoal);
  }
  .offer-text {
    position: absolute; left: 36px; top: 26px;
    font-weight: 800; font-size: 26px; color: var(--white);
  }
  .offer-text .accent { color: var(--lime); }

  .contact-band {
    position: absolute; left: 350px; top: 300px; width: 850px; height: 80px;
    background: var(--lime);
    clip-path: polygon(28px 0, 100% 0, 100% 100%, 28px 100%, 0 50%);
    display: flex; align-items: center; padding-left: 54px; gap: 14px;
    color: var(--white);
  }
  .contact-phone { font-weight: 800; font-size: 44px; display: flex; align-items: center; gap: 10px; }
  .contact-web { font-weight: 800; font-size: 20px; display: flex; align-items: center; gap: 10px; margin-left: 14px; }

  .photo-zone {
    position: absolute; border-radius: 48% 52% 44% 56% / 56% 44% 56% 44%;
    background: radial-gradient(ellipse at 50% 50%, #8f8476 0%, #b5aa9c 45%, var(--mint) 78%);
  }
  .photo-zone.squirrel { left: 440px; top: 70px; width: 260px; height: 225px; }
  .photo-zone.rat {
    left: 740px; top: 80px; width: 430px; height: 120px;
    background: radial-gradient(ellipse at 45% 50%, #6e5540 0%, #9a8068 45%, var(--mint) 78%);
  }

  .services {
    position: absolute; left: 700px; top: 212px; width: 480px;
    display: flex; justify-content: space-between;
  }
  .service { display: flex; flex-direction: column; align-items: center; width: 90px; gap: 6px; }
  .service svg { width: 40px; height: 40px; }
  .service-label { font-family: "Poppins", sans-serif; font-weight: 500; font-size: 13px; color: var(--ink); white-space: nowrap; }
</style>
</head>
<body>
  <main class="billboard">
    <div class="mint-blob left"></div>
    <div class="mint-blob right"></div>
    <div class="photo-zone squirrel" role="img" aria-label="Photo of a grey squirrel sitting upright with paws together"></div>
    <div class="photo-zone rat" role="img" aria-label="Photo of a brown rat walking, seen from the side"></div>

    <header class="brand">
      <div class="brand-name"><span class="brand-dot"></span>Tovally's Pest Control LLC</div>
      <div class="brand-phone">(555)014-2208</div>
    </header>

    <p class="quip">Cute? Sure. Rent-paying? Never.<br><span class="accent">We'll handle the eviction, politely.</span></p>

    <h1 class="headline">
      Eliminate Pests<br>
      Fast with Reliable<br>
      <span class="accent">Expert Pest Control!</span>
    </h1>

    <section class="services">
      <div class="service">
        <svg viewBox="0 0 40 40" fill="none" stroke="var(--lime-deep)" stroke-width="3.5" stroke-linecap="round" stroke-linejoin="round">
          <circle cx="23" cy="16" r="11"/><path d="M15 24 6 33"/><path d="m18 16 4 4 6-7"/>
        </svg>
        <span class="service-label">Inspection</span>
      </div>
      <div class="service">
        <svg viewBox="0 0 40 40" fill="none" stroke="var(--lime-deep)" stroke-width="2.5">
          <path d="M20 3 36 12v16L20 37 4 28V12z"/><path d="M12 7v27M20 3v34M28 7v27M4 16h32M4 24h32"/>
        </svg>
        <span class="service-label">Trapping</span>
      </div>
      <div class="service">
        <svg viewBox="0 0 40 40">
          <path d="M20 3 34 8v12c0 9-6 14-14 17C12 34 6 29 6 20V8z" fill="var(--lime-deep)"/>
          <ellipse cx="20" cy="21" rx="5" ry="7" fill="var(--white)"/>
          <circle cx="31" cy="31" r="7" fill="var(--lime)"/>
          <path d="m28 31 2 2 4-4" stroke="var(--white)" stroke-width="2" fill="none"/>
        </svg>
        <span class="service-label">Removal</span>
      </div>
      <div class="service">
        <svg viewBox="0 0 40 40" fill="var(--lime-deep)">
          <rect x="14" y="16" width="12" height="22" rx="3"/><rect x="15" y="8" width="14" height="7" rx="2"/>
          <rect x="29" y="9" width="6" height="4"/><circle cx="6" cy="7" r="1.6"/><circle cx="10" cy="11" r="1.6"/><circle cx="6" cy="14" r="1.6"/>
        </svg>
        <span class="service-label">Sanitization</span>
      </div>
      <div class="service">
        <svg viewBox="0 0 40 40" fill="var(--lime-deep)">
          <rect x="24" y="3" width="6" height="16" rx="2" transform="rotate(40 27 11)"/>
          <path d="M20 17 27 24 18 33 8 30 6 28z"/>
          <circle cx="26" cy="34" r="1.8"/><circle cx="31" cy="31" r="1.8"/>
        </svg>
        <span class="service-label">Attic Cleaning</span>
      </div>
    </section>

    <div class="offer-band">
      <p class="offer-text"><span class="accent">For FREE</span> Inspections!</p>
    </div>

    <footer class="contact-band">
      <span class="contact-phone">
        <svg width="26" height="32" viewBox="0 0 24 30" fill="var(--white)"><path d="M6 2h5l1 7-4 2c1 4 3 7 6 9l3-3 6 2v5c-2 3-5 4-8 2C8 22 4 15 3 8 3 5 4 3 6 2z"/></svg>
        555-013-7291
      </span>
      <span class="contact-web">
        <svg width="30" height="30" viewBox="0 0 30 30" fill="none" stroke="var(--white)" stroke-width="2"><circle cx="15" cy="15" r="12"/><ellipse cx="15" cy="15" rx="5" ry="12"/><path d="M3 15h24M5 9h20M5 21h20"/></svg>
        WWW.TOVALLYS-EXAMPLE.COM
      </span>
    </footer>
  </main>
</body>
</html>
```